Rd Yallen - Outback Australia (Working farm, film location and farmstay promotation)

I need a website to promote my film location and farm stay business. Would like the ability to have online booking also and payment options

REFER TO
https://vw.scenefinder.net/location_detail.aspx?id=058-20493615&search=dry%20creek&search_mode=and&ctry=all&state=&city=&cat=&subcat=&style=&lname=&locid=&int=&parent=search_results

https://www.facebook.com/pg/redyallenholding/photos/?ref=page_internal

Target Market(s)

International Tourists
Film crews

Coding

Coded - Design and coding required

Number of Pages Required

1 page

Colors

Designer to choose colors to be used in the design.

Requirements
Must have
• Ability for online booking

```html
<!DOCTYPE html>
<html lang="en">
<head>
<meta charset="utf-8">
<title>Rd Yallen Station Stay</title>
<link href="https://fonts.googleapis.com/css2?family=Lato:wght@400;700;900&family=Catamaran:wght@600;700;800&display=swap" rel="stylesheet">
<style>
:root{
  --orange:#ff6a0a;
  --orange-soft:#fdb58a;
  --yellow:#fcd34d;
  --navy:#2d3047;
  --ink:#1d1d24;
  --text:#4a4a52;
  --line:#e4e4ea;
  --white:#ffffff;
  --field:#f3f3f5;
}
*{box-sizing:border-box;margin:0;padding:0}
html,body{width:1200px;height:3635px;overflow:hidden}
body{background:var(--orange);font-family:"Lato",sans-serif;color:var(--text);position:relative}
.page{position:absolute;left:56px;top:114px;width:1089px;height:3406px;background:var(--white);overflow:hidden}
.abs{position:absolute}
h1,h2,h3{font-family:"Catamaran",sans-serif;color:var(--ink)}
.btn{position:absolute;display:flex;align-items:center;justify-content:center;font-size:11px;letter-spacing:.3px;color:var(--white);background:var(--orange);border-radius:4px;box-shadow:0 4px 10px rgba(255,106,10,.35);text-transform:uppercase}
.eyebrow{position:absolute;font-size:10px;letter-spacing:2px;color:var(--orange);text-transform:uppercase}
.para{position:absolute;font-size:10.5px;line-height:24px;color:var(--text)}
.photo{position:absolute}

/* nav */
.brand-name{position:absolute;left:155px;top:34px;font-family:"Lato",sans-serif;font-weight:700;font-size:17px;color:var(--ink);line-height:1}
.nav{position:absolute;left:385px;top:37px;display:flex;gap:39px;font-size:11px;color:var(--ink)}
.btn-register{left:739px;top:28px;width:98px;height:32px}
.btn-book{left:845px;top:28px;width:98px;height:32px;background:var(--yellow);color:var(--ink);box-shadow:0 4px 10px rgba(252,211,77,.45)}

/* hero */
.hero-photo{left:0;top:88px;width:1089px;height:500px;background:linear-gradient(180deg,#8fa7c4 0%,#c7d3e0 45%,#b9784a 68%,#c2653a 100%)}
.hero-title{position:absolute;left:150px;top:236px;font-size:56px;font-weight:700;color:var(--white);letter-spacing:1px;line-height:70px}
.hero-text{position:absolute;left:150px;top:312px;width:380px;font-size:12.5px;line-height:25px;color:var(--white)}
.btn-hero{left:150px;top:382px;width:105px;height:30px}

/* framed photos */
.frame-back{position:absolute;background:var(--orange-soft);border-radius:0 40px 40px 0}
.frame-edge{position:absolute;border:3px solid var(--yellow);border-radius:0 40px 40px 0}
.frame-photo{position:absolute;border-radius:0 38px 38px 0;overflow:hidden}

/* category */
.cat-title{position:absolute;left:0;width:1089px;text-align:center}
.grid{position:absolute;left:127px;top:1127px;width:835px;height:458px;display:grid;grid-template-columns:203px 215px 214px 203px;grid-template-rows:229px 229px}
.cell{position:relative;text-align:center;border-right:1px solid var(--line);border-bottom:1px solid var(--line)}
.cell:nth-child(4n){border-right:none}
.cell:nth-child(n+5){border-bottom:none}
.cell svg{margin-top:30px;width:64px;height:64px}
.cell h3{font-family:"Lato",sans-serif;font-weight:700;font-size:14px;margin-top:12px;color:var(--ink)}
.cell p{font-size:9px;line-height:18px;margin:10px auto 0;width:170px;color:var(--text)}
.cell.active{background:var(--orange)}
.cell.active h3,.cell.active p{color:var(--white)}

/* testimonials */
.quote{position:absolute;width:152px;height:150px;border:1px solid #dcdce2;border-radius:4px;background:var(--white);padding:12px 13px}
.quote .mark{font-family:"Catamaran",sans-serif;font-size:20px;color:var(--ink);line-height:14px}
.quote p{font-size:8.5px;line-height:18px;color:var(--text);margin-top:4px}
.quote .who{font-size:9.5px;color:var(--orange);margin-top:6px}
.quote .role{font-size:8.5px;color:var(--ink);font-weight:700}
.quote .avatar{position:absolute;right:12px;bottom:-8px;width:34px;height:34px;border-radius:50%;background:linear-gradient(#e9c9a8,#c98c6a);border:2px solid var(--white)}
.arrow{position:absolute;width:40px;height:40px;border:1px solid var(--orange);border-radius:3px;display:flex;align-items:center;justify-content:center;color:var(--orange);font-size:16px}
.arrow.next{background:var(--orange);color:var(--white)}

/* booking */
.booking-photo{left:0;top:2424px;width:1089px;height:620px;background:linear-gradient(120deg,#eef3f8 0%,#dfe7ef 40%,#c7d6e6 70%,#a9bfd6 100%)}
.form{position:absolute;left:127px;top:2536px;width:335px;height:410px;background:var(--white);box-shadow:0 6px 24px rgba(0,0,0,.12)}
.form-head{height:60px;background:var(--navy);color:var(--white);font-family:"Catamaran",sans-serif;font-weight:600;font-size:26px;display:flex;align-items:center;justify-content:center;letter-spacing:.5px}
.field{position:absolute;left:14px;width:307px;height:48px;border:1px solid #d8d8de;border-radius:4px;background:var(--field);font-size:10px;color:#a6a6ae;padding:0 28px;display:flex;align-items:center}
.field.focus{background:var(--white);border-color:var(--orange)}
.btn-submit{left:14px;top:346px;width:307px;height:47px;font-size:14px;border-radius:3px;box-shadow:none}

/* footer */
.footer-brand{position:absolute;left:145px;top:3100px;font-family:"Lato",sans-serif;font-weight:700;font-size:22px;color:var(--white);line-height:1}
.footer-text{position:absolute;font-size:10.5px;color:var(--white);text-transform:uppercase}
.social{position:absolute;top:3153px;left:145px;display:flex;gap:11px}
.social span{width:25px;height:25px;border:1px solid #8a8ca0;border-radius:50%}
.rule{position:absolute;left:127px;top:3277px;width:835px;height:1px;background:#5a5d72}
.cta{position:absolute;left:139px;top:3306px;font-family:"Catamaran",sans-serif;font-weight:700;font-size:30px;line-height:36px;color:var(--white)}
.cta em{font-style:normal;color:var(--orange)}
.email{position:absolute;left:593px;top:3319px;width:248px;height:40px;background:var(--white);border-radius:3px;font-size:10px;color:#a6a6ae;display:flex;align-items:center;padding-left:22px}
.btn-sub{left:852px;top:3319px;width:110px;height:40px;font-size:13px;font-weight:700;box-shadow:none}
</style>
</head>
<body>
<main class="page">

  <!-- navigation -->
  <header>
    <span class="brand-name">Rd Yallen</span>
    <nav class="nav"><span>HOME</span><span>ABOUT US</span><span>TESTIMONIALS</span><span>LOG IN</span></nav>
    <span class="btn btn-register">Register</span>
    <span class="btn btn-book">Book Now</span>
  </header>

  <!-- hero -->
  <section>
    <div class="photo hero-photo" role="img" aria-label="Outback plain with red earth, low scrub and a lone tree under a blue sky"></div>
    <svg class="abs" style="left:0;top:470px" width="1089" height="120" viewBox="0 0 1089 120">
      <path d="M0 70 C200 40 380 60 520 55 C680 48 760 -20 900 40 C980 75 1040 60 1089 38 L1089 120 L0 120 Z" fill="#fff"/>
      <path d="M0 70 C140 50 260 48 380 54 C250 56 120 66 0 80 Z" fill="var(--orange)"/>
      <path d="M960 62 C1010 58 1050 48 1089 36 L1089 44 C1050 58 1010 64 960 62 Z" fill="var(--yellow)"/>
    </svg>
    <h1 class="hero-title">RD YALLEN</h1>
    <p class="hero-text">Lorem ipsum dolor sit amet, consectetur adipiscing elit, sed do eiusmod tempor incididunt ut labore</p>
    <span class="btn btn-hero">Book Now</span>
  </section>

  <!-- about -->
  <section>
    <div class="frame-back" style="left:15px;top:628px;width:470px;height:320px;transform:rotate(1.2deg)"></div>
    <div class="frame-edge" style="left:0;top:634px;width:496px;height:318px"></div>
    <div class="frame-photo photo" style="left:0;top:638px;width:487px;height:308px;background:linear-gradient(180deg,#8cb6e0 0%,#d8e6f2 30%,#8a5a3c 55%,#5a4636 75%,#6f6052 100%)" role="img" aria-label="Rocky gorge with a creek pool and a hiker resting on the rocks"></div>
    <span class="eyebrow" style="left:533px;top:701px">About Us</span>
    <h2 class="abs" style="left:533px;top:720px;font-size:30px;font-weight:700">CONSECTETUR ADIPISCING</h2>
    <p class="para" style="left:533px;top:778px;width:420px">Rd Yallen Station is an 85,000 acre sheep and cattle property about 40kms/30 minute drive north of the regional city of Dry Creek. Features include hills, gorges, mines, rock formations and creeks</p>
    <span class="btn" style="left:536px;top:877px;width:105px;height:30px">Learn More</span>
  </section>

  <!-- category -->
  <section>
    <svg class="abs" style="left:-10px;top:940px" width="520" height="520" viewBox="0 0 520 520"><circle cx="250" cy="260" r="215" fill="none" stroke="#f4f5f8" stroke-width="30"/></svg>
    <span class="eyebrow cat-title" style="top:1018px">Category</span>
    <h2 class="cat-title" style="top:1042px;font-size:30px;font-weight:700">LOCATION CATEGORY</h2>
    <div class="grid">
      <div class="cell">
        <svg viewBox="0 0 64 64" fill="none" stroke="var(--orange)" stroke-width="2"><circle cx="34" cy="30" r="24" fill="#f6f6f9" stroke="none"/><rect x="18" y="16" width="28" height="38"/><path d="M24 22h4M36 22h4M24 30h4M36 30h4M24 38h4M36 38h4M28 54v-8h8v8"/></svg>
        <h3>ACCOMMODATIONS</h3><p>Lorem ipsum dolor sit amet, consectetur adipiscing elit, sed do eiu</p>
      </div>
      <div class="cell active">
        <svg viewBox="0 0 64 64" fill="none" stroke="#fff" stroke-width="2"><circle cx="34" cy="30" r="24" fill="rgba(255,255,255,.25)" stroke="none"/><circle cx="32" cy="34" r="16"/><path d="M32 46V24M32 30l-6-4M32 30l6-4M32 37l-6-4M32 37l6-4"/></svg>
        <h3>AGRICULTURE</h3><p>Lorem ipsum dolor sit amet, consectetur adipiscing elit, sed do eiu</p>
      </div>
      <div class="cell">
        <svg viewBox="0 0 64 64" fill="none" stroke="var(--orange)" stroke-width="2"><circle cx="34" cy="30" r="24" fill="#f6f6f9" stroke="none"/><path d="M10 34L32 14l22 20M16 29v24h32V29M27 53V40h10v13"/></svg>
        <h3>HOUSES</h3><p>Lorem ipsum dolor sit amet, consectetur adipiscing elit, sed do eiu</p>
      </div>
      <div class="cell">
        <svg viewBox="0 0 64 64" fill="none" stroke="var(--orange)" stroke-width="2"><circle cx="34" cy="30" r="24" fill="#f6f6f9" stroke="none"/><path d="M12 54V36l10-6v6l10-6v6l10-6V14h6v40Z"/><path d="M18 44h4M28 44h4M38 44h4"/></svg>
        <h3>INDUSTRIAL</h3><p>Lorem ipsum dolor sit amet, consectetur adipiscing elit, sed do eiu</p>
      </div>
      <div class="cell">
        <svg viewBox="0 0 64 64" fill="none" stroke="var(--orange)" stroke-width="2"><circle cx="34" cy="30" r="24" fill="#f6f6f9" stroke="none"/><circle cx="28" cy="24" r="6"/><path d="M6 54h52M10 54l14-16 10 10 8-8 14 14M48 40V28M44 34h8"/></svg>
        <h3>LANDSCAPES</h3><p>Lorem ipsum dolor sit amet, consectetur adipiscing elit, sed do eiu</p>
      </div>
      <div class="cell">
        <svg viewBox="0 0 64 64" fill="none" stroke="var(--orange)" stroke-width="2"><circle cx="34" cy="30" r="24" fill="#f6f6f9" stroke="none"/><path d="M16 54V38M16 38l-6-12 6-12 6 12Z M48 54V40M48 40a6 8 0 1 1 0-16 6 8 0 1 1 0 16M24 46h16M26 46v8M38 46v8M32 18v28"/></svg>
        <h3>PARKS</h3><p>Lorem ipsum dolor sit amet, consectetur adipiscing elit, sed do eiu</p>
      </div>
      <div class="cell">
        <svg viewBox="0 0 64 64" fill="none" stroke="var(--orange)" stroke-width="2"><circle cx="34" cy="30" r="24" fill="#f6f6f9" stroke="none"/><path d="M26 10L14 56M38 10l12 46M32 14v6M32 26v6M32 38v6M32 50v6"/></svg>
        <h3>ROADS / HIGHWAYS</h3><p>Lorem ipsum dolor sit amet, consectetur adipiscing elit, sed do eiu</p>
      </div>
      <div class="cell">
        <svg viewBox="0 0 64 64" fill="none" stroke="var(--orange)" stroke-width="2"><circle cx="34" cy="30" r="24" fill="#f6f6f9" stroke="none"/><path d="M8 44c12-8 30-10 48-4M10 52c14-6 28-6 42 0M34 36V24l8-6 8 6v12M44 24a6 6 0 1 0-12 0"/></svg>
        <h3>FARM</h3><p>Lorem ipsum dolor sit amet, consectetur adipiscing elit, sed do eiu</p>
      </div>
    </div>
  </section>

  <!-- video -->
  <section>
    <span class="eyebrow" style="left:144px;top:1708px">Our Portfolio</span>
    <h2 class="abs" style="left:144px;top:1726px;font-size:30px;font-weight:700">VIDEO</h2>
    <p class="para" style="left:144px;top:1786px;width:420px">Vivamus augue velit, faucibus non aliquet vel, rutrum eget dolor. Praesent non elit vitae lorem efficitur faucibus. Nam pretium dignissim felis, non tincidunt risus volutpat vel. Praesent pellentesque dolor mi</p>
    <span class="btn" style="left:147px;top:1884px;width:105px;height:30px">Learn More</span>
    <div class="abs" style="left:590px;top:1640px;width:505px;height:10px;background:var(--orange-soft);transform:rotate(-1.5deg)"></div>
    <div class="abs" style="left:591px;top:1658px;width:510px;height:308px;background:var(--orange-soft);border-radius:38px 0 0 38px;transform:rotate(-1deg)"></div>
    <div class="abs" style="left:596px;top:1652px;width:500px;height:308px;border:3px solid var(--yellow);border-radius:38px 0 0 38px"></div>
    <div class="photo" style="left:604px;top:1646px;width:485px;height:302px;border-radius:36px 0 0 36px;background:linear-gradient(180deg,#4b5566 0%,#505056 45%,#3b3a3c 70%,#2d2c2e 100%)" role="img" aria-label="Film crew gathered beside a coach bus on a dusty outback lot"></div>
    <svg class="abs" style="left:813px;top:1768px" width="58" height="58" viewBox="0 0 58 58"><circle cx="29" cy="29" r="29" fill="#d9352a"/><path d="M22 17l20 12-20 12Z" fill="#fff"/></svg>
  </section>

  <!-- testimonials -->
  <section>
    <div class="frame-back" style="left:15px;top:2045px;width:470px;height:320px;transform:rotate(1.2deg)"></div>
    <div class="frame-edge" style="left:0;top:2050px;width:496px;height:318px"></div>
    <div class="frame-photo photo" style="left:0;top:2052px;width:487px;height:308px;background:linear-gradient(180deg,#4f5a70 0%,#8a8c96 45%,#c9a58a 75%,#e6b88f 100%)" role="img" aria-label="Friends jumping against a dusk sky beside a bare tree"></div>
    <span class="eyebrow" style="left:542px;top:2084px">Testimonials</span>
    <h2 class="abs" style="left:542px;top:2102px;font-size:30px;font-weight:700">THEY MEMORIZED THAT</h2>
    <div class="quote" style="left:542px;top:2162px">
      <div class="mark">&ldquo;</div>
      <p>Lorem ipsum dolor sit amet, consectetur adipiscing elit, sed do eiusmod tempor incididunt ut labore et dolore</p>
      <div class="who">NORA FINCH</div><div class="role">Designation</div>
      <span class="avatar" role="img" aria-label="Guest portrait"></span>
    </div>
    <div class="quote" style="left:715px;top:2162px">
      <div class="mark">&ldquo;</div>
      <p>Lorem ipsum dolor sit amet, consectetur adipiscing elit, sed do eiusmod tempor incididunt ut labore et dolore</p>
      <div class="who">NORA FINCH</div><div class="role">Designation</div>
      <span class="avatar" role="img" aria-label="Guest portrait"></span>
    </div>
    <span class="arrow" style="left:545px;top:2344px">&larr;</span>
    <span class="arrow next" style="left:600px;top:2344px">&rarr;</span>
  </section>

  <!-- booking -->
  <section>
    <div class="photo booking-photo" role="img" aria-label="Smiling man working on a laptop in a bright office"></div>
    <svg class="abs" style="left:0;top:2400px" width="1089" height="60" viewBox="0 0 1089 60">
      <path d="M0 0H1089V20C980 40 880 10 760 24 600 44 480 4 320 20 200 32 100 14 0 30Z" fill="#fff"/>
      <path d="M0 30C100 14 200 32 320 20 480 4 600 44 760 24 880 10 980 40 1089 20V26C980 46 880 18 760 32 600 52 480 12 320 28 200 40 100 22 0 36Z" fill="#fbeedd"/>
    </svg>
    <div class="form">
      <div class="form-head">ONLINE BOOKING</div>
      <div class="field focus" style="top:83px">Name</div>
      <div class="field" style="top:149px">Arival</div>
      <div class="field" style="top:214px">Categories</div>
      <div class="field" style="top:276px">Detail</div>
      <span class="btn btn-submit">Book Now</span>
    </div>
  </section>

  <!-- footer -->
  <footer>
    <svg class="abs" style="left:0;top:2950px" width="1089" height="456" viewBox="0 0 1089 456">
      <path d="M0 60C120 30 240 10 380 40 520 70 600 110 720 80 860 44 980 20 1089 40V456H0Z" fill="var(--navy)"/>
      <path d="M0 60C120 30 240 10 380 40 300 24 150 34 0 54Z" fill="#f3d9b8"/>
      <path d="M720 80C860 44 980 20 1089 40V32C980 12 860 36 720 80Z" fill="#f3d9b8"/>
    </svg>
    <span class="footer-brand">Rd Yallen</span>
    <div class="social"><span></span><span></span><span></span><span></span><span></span></div>
    <span class="footer-text" style="left:147px;top:3220px;font-size:10px">&copy;&nbsp;&nbsp;Copyright 2019 Rd Yallen</span>
    <span class="footer-text" style="left:447px;top:3127px">Home</span>
    <span class="footer-text" style="left:447px;top:3158px">About Us</span>
    <span class="footer-text" style="left:447px;top:3189px">Services</span>
    <span class="footer-text" style="left:447px;top:3220px">Contact Us</span>
    <svg class="abs" style="left:659px;top:3125px" width="16" height="16" viewBox="0 0 24 24" fill="none" stroke="#fff" stroke-width="1.6"><path d="M5 3h4l2 5-2.5 1.5a11 11 0 0 0 6 6L16 13l5 2v4a2 2 0 0 1-2 2A16 16 0 0 1 3 5a2 2 0 0 1 2-2z"/></svg>
    <span class="footer-text" style="left:686px;top:3127px">Phone: +61 2 8000 4172</span>
    <svg class="abs" style="left:660px;top:3187px" width="14" height="18" viewBox="0 0 24 30" fill="none" stroke="#fff" stroke-width="1.8"><path d="M12 28S3 18 3 11a9 9 0 0 1 18 0c0 7-9 17-9 17z"/><circle cx="12" cy="11" r="3.5"/></svg>
    <span class="footer-text" style="left:686px;top:3189px">Red Yallen Station</span>
    <span class="footer-text" style="left:686px;top:3220px">Dry Creek, NSW 2890</span>
    <div class="rule"></div>
    <div class="cta"><em>GET MORE UPDATES</em> &amp; GET<br>IN TOUCH</div>
    <div class="email">Enter Your Email...</div>
    <span class="btn btn-sub">Subscribe</span>
  </footer>

</main>
</body>
</html>
```